brovalux business card

We are a commercial cleaning/janitorial service company our main target is building owners and managers.
Would like to see the icon as a background shadow in the front and the full logo in white on the back with a blue background.  On the card:
Dorn Pevsky, Operations Manager, dorn@brovalux-example.com
47215-K Harlow Ave. 9 #382
Pinecrest, IN 47912
555.604.2817, 888.555.4163

Updates
please include cell 555.318.6247
                                   
Thank you
If possible the fading logo on the front should be very subtle and light and lets look at centering that as well
thanks

```html
<!DOCTYPE html>
<html lang="en">
<head>
<meta charset="utf-8">
<title>brovalux business card</title>
<link href="https://fonts.googleapis.com/css2?family=Arimo:wght@400;700&family=Open+Sans:wght@400;600&display=swap" rel="stylesheet">
<style>
  :root {
    --page-bg: #e4e6e9;
    --brand-blue: #1c6fb8;
    --deep-blue: #0d4f8c;
    --bright-blue: #2a8ad8;
    --charcoal: #3a3b3e;
    --ink: #333333;
    --rule: #9fb8d2;
    --white: #ffffff;
  }
  * { box-sizing: border-box; margin: 0; padding: 0; }
  html, body { width: 1200px; height: 901px; overflow: hidden; }
  body {
    background: var(--page-bg);
    font-family: "Open Sans", sans-serif;
    position: relative;
  }
  .card {
    position: absolute;
    left: 240px;
    width: 720px;
    height: 412px;
    border-radius: 26px;
    overflow: hidden;
    box-shadow: 0 6px 18px rgba(0,0,0,0.18);
  }
  /* Back */
  .card-back {
    top: 24px;
    background: radial-gradient(ellipse at 42% 45%, var(--bright-blue) 0%, var(--brand-blue) 35%, var(--deep-blue) 100%);
  }
  .back-logo {
    position: absolute;
    left: 0; right: 0; top: 150px;
    display: flex; align-items: center; justify-content: center; gap: 22px;
  }
  .back-logo .mark { width: 84px; height: 84px; border-radius: 50%; background: var(--white); }
  .back-logo .wordmark {
    font-family: "Arimo", sans-serif; font-weight: 700; font-size: 86px;
    color: var(--white); letter-spacing: -1px; line-height: 1;
  }
  .back-url {
    position: absolute; right: 48px; bottom: 30px;
    font-size: 17px; color: var(--white);
  }
  /* Front */
  .card-front { top: 466px; background: var(--white); }
  .front-logo {
    position: absolute; left: 0; right: 0; top: 38px;
    display: flex; align-items: center; justify-content: center; gap: 14px;
  }
  .front-logo .mark { width: 60px; height: 60px; border-radius: 50%; background: var(--brand-blue); }
  .front-logo .wordmark {
    font-family: "Arimo", sans-serif; font-weight: 700; font-size: 62px;
    color: var(--brand-blue); letter-spacing: -1px; line-height: 1;
  }
  .person { position: absolute; left: 56px; top: 172px; font-family: "Arimo", sans-serif; }
  .person .name { font-size: 22px; font-weight: 700; color: var(--brand-blue); }
  .person .title { font-size: 15px; color: var(--ink); margin-top: 2px; }
  .address {
    position: absolute; left: 56px; top: 246px;
    font-family: "Arimo", sans-serif; font-size: 18px; line-height: 1.3; color: var(--brand-blue);
  }
  .divider { position: absolute; left: 360px; top: 170px; width: 2px; height: 130px; background: var(--rule); }
  .contacts { position: absolute; left: 382px; top: 172px; list-style: none; }
  .contacts li {
    display: flex; align-items: center; gap: 12px;
    font-size: 18px; color: var(--ink); height: 30px;
  }
  .contacts svg { width: 18px; height: 18px; fill: var(--brand-blue); flex: none; }
  .front-band { position: absolute; left: 0; bottom: 0; width: 720px; height: 72px; }
</style>
</head>
<body>

<section class="card card-back" aria-label="Card back">
  <div class="back-logo">
    <span class="mark"></span>
    <span class="wordmark">brovalux</span>
  </div>
  <p class="back-url">www.brovalux-example.com</p>
</section>

<section class="card card-front" aria-label="Card front">
  <div class="front-logo">
    <span class="mark"></span>
    <span class="wordmark">brovalux</span>
  </div>

  <div class="person">
    <p class="name">Dorn Pevsky</p>
    <p class="title">Operations Manager</p>
  </div>

  <p class="address">47215-K Harlow Ave. 9 #382<br>Pinecrest, IN 47912</p>

  <div class="divider"></div>

  <ul class="contacts">
    <li>
      <svg viewBox="0 0 24 24" aria-hidden="true"><path d="M3 7c0-2 3-4 9-4s9 2 9 4v2h-5V7H8v2H3zM6 11h12l2 8H4z"/></svg>
      555.604.2817 / 888.555.4163
    </li>
    <li>
      <svg viewBox="0 0 24 24" aria-hidden="true"><path d="M7 1h10a2 2 0 0 1 2 2v18a2 2 0 0 1-2 2H7a2 2 0 0 1-2-2V3a2 2 0 0 1 2-2zm1 3v11h8V4zm4 14a1.5 1.5 0 1 0 0 3 1.5 1.5 0 0 0 0-3z"/></svg>
      555.318.6247
    </li>
    <li>
      <svg viewBox="0 0 24 24" aria-hidden="true"><path d="M2 5h20v14H2zm2 2v1l8 5 8-5V7l-8 5z"/></svg>
      dorn@brovalux-example.com
    </li>
    <li>
      <svg viewBox="0 0 24 24" aria-hidden="true"><path d="M12 2a10 10 0 1 0 0 20 10 10 0 0 0 0-20zm-1 2.1V8H7.3A8 8 0 0 1 11 4.1zm2 0A8 8 0 0 1 16.7 8H13zM4.3 10H11v4H4.3a8 8 0 0 1 0-4zm8.7 0h6.7a8 8 0 0 1 0 4H13zm-5.7 6H11v3.9A8 8 0 0 1 7.3 16zm5.7 0h3.7a8 8 0 0 1-3.7 3.9z"/></svg>
      www.brovalux-example.com
    </li>
  </ul>

  <svg class="front-band" viewBox="0 0 720 72" preserveAspectRatio="none" aria-hidden="true">
    <polygon points="0,48 440,48 462,72 0,72" fill="var(--brand-blue)"/>
    <polygon points="440,48 720,48 720,72 462,72" fill="var(--charcoal)"/>
    <polygon points="440,30 720,30 720,48 440,48" fill="var(--charcoal)"/>
    <polygon points="0,30 424,30 440,48 0,48" fill="var(--white)"/>
  </svg>
</section>

</body>
</html>
```